Saltwater In store poster design

We need a poster design that will be hung in aquarium stores, to advertise that they use our natural saltwater.

Must use logo as well as be bright and colourful. We are trying to communicate that the water is natural (so good for your marine tank) as well as clean and safe, so please consider this in your design.

Must say something along the lines of "We use natural ocean water supplied by Reef Bucket in our store" as well as "you can purchase natural ocean water here"

Open to all design types and suggestions as we will update the brief if we find one specific style that we prefer.

Target Market(s)

Customers who own marine aquariums

Industry/Entity Type

Store

Requirements
Must have
• Reef bucket logo (does not need to have blue background attached, just the oval)

Be eye catching

Have similar phrases to those above

```html
<!DOCTYPE html>
<html lang="en">
<head>
<meta charset="utf-8">
<title>Natural Ocean Water – In-store Poster</title>
<link rel="stylesheet" href="https://fonts.googleapis.com/css2?family=Anton&family=Archivo+Black&family=Poppins:wght@300;700;800;900&display=swap">
<style>
  :root {
    --page: #ffffff;
    --frame: #555555;
    --ink: #111111;
    --ocean-blue: #0b4f9e;
    --brand-blue: #1f7fd1;
    --water-deep: #1d5f9a;
    --water-mid: #5aa8d6;
    --water-light: #d6ecf7;
    --white: #ffffff;
  }
  html, body {
    margin: 0;
    padding: 0;
    width: 1200px;
    height: 900px;
    overflow: hidden;
    background: var(--page);
  }
  .canvas {
    position: relative;
    width: 1200px;
    height: 900px;
  }
  .poster {
    position: absolute;
    left: 0;
    top: 0;
  }
  .headline-intro { font-family: "Poppins", sans-serif; font-weight: 900; fill: var(--ink); }
  .headline-condensed { font-family: "Anton", sans-serif; }
  .headline-water { font-family: "Archivo Black", sans-serif; fill: var(--white); }
  .headline-here { font-family: "Poppins", sans-serif; font-weight: 800; fill: var(--white); }
  .supplier-label { font-family: "Poppins", sans-serif; font-weight: 300; fill: var(--ink); }
  .brand-name { font-family: "Poppins", sans-serif; font-weight: 700; fill: var(--brand-blue); }
  .brand-dot { fill: var(--brand-blue); }
</style>
</head>
<body>
<main class="canvas">
  <svg class="poster" width="1200" height="900" viewBox="0 0 1200 900" xmlns="http://www.w3.org/2000/svg">
    <defs>
      <linearGradient id="ocean-fill" x1="0" y1="0" x2="1" y2="1">
        <stop offset="0" stop-color="var(--water-deep)"/>
        <stop offset="0.45" stop-color="var(--water-mid)"/>
        <stop offset="0.75" stop-color="var(--water-light)"/>
        <stop offset="1" stop-color="var(--water-mid)"/>
      </linearGradient>
    </defs>

    <rect class="poster-sheet" x="304.5" y="37.5" width="594" height="840" fill="var(--page)" stroke="var(--frame)" stroke-width="1"/>

    <text class="headline-intro" x="593" y="125" font-size="82" text-anchor="middle" textLength="305" lengthAdjust="spacingAndGlyphs">you can</text>
    <text class="headline-intro" x="606" y="190" font-size="82" text-anchor="middle" textLength="358" lengthAdjust="spacingAndGlyphs">purchase</text>

    <polygon class="ocean-banner" points="307,210 896,210 896,610 592,722 307,610" fill="var(--ocean-blue)"/>

    <g role="img" aria-label="Lettering filled with an underwater photo of splashing sea water and bubbles">
      <text class="headline-condensed" x="363" y="364" font-size="178" textLength="472" lengthAdjust="spacingAndGlyphs"
            fill="url(#ocean-fill)" stroke="var(--white)" stroke-width="3" paint-order="stroke">natural</text>
      <text class="headline-condensed" x="364" y="494" font-size="178" textLength="470" lengthAdjust="spacingAndGlyphs"
            fill="url(#ocean-fill)" stroke="var(--white)" stroke-width="3" paint-order="stroke">ocean</text>
    </g>

    <text class="headline-water" x="608" y="600" font-size="128" text-anchor="middle" textLength="404" lengthAdjust="spacingAndGlyphs">water</text>
    <text class="headline-here" x="602" y="686" font-size="70" text-anchor="middle" textLength="170" lengthAdjust="spacingAndGlyphs">here</text>

    <text class="supplier-label" x="373" y="808" font-size="30" textLength="180" lengthAdjust="spacingAndGlyphs">supplied by</text>

    <g class="brand-mark">
      <circle class="brand-dot" cx="612" cy="797" r="10"/>
      <text class="brand-name" x="630" y="812" font-size="40" textLength="212" lengthAdjust="spacingAndGlyphs">Reef Bucket</text>
    </g>
  </svg>
</main>
</body>
</html>
```